依頼詳細
サイトの特徴としては東京都内の賃料15万円以上のマンションを中心に掲載しているサイトになります。

高級感、安心感のあるバナーを希望します。
バナーからのリンクはサイトトップページに遷移させます。
サイト:碧泉荘館 https://www.hekisen-k.net/
サイト特徴説明: https://www.hekisen-k.net/guide

記載項目
素材は特にありませんので、ご提案いただけると幸いです。
記載したい文言は以下です。サイト名は必須でお願いします。
それ以外は必須ではありません。

サイト名:高級賃貸の碧泉荘館

高級賃貸を賢く探すなら
都心の高級賃貸検索サイト
仲介料が最大無料の高級賃貸検索サイト

サイズ
• 300 x 250 ( ミディアムレクタングル )
• 250 x 250 ( スクエアポップアップ )
• 160 x 600 ( ワイドスカイスクレイパー )
• 160×600 468×60  320×50  320×100
希望イメージ
シンプル 複雑
単色 カラフル
暗い 明るい
日常 高級
遊び心 厳粛
未来的 伝統的
女性的 男性的
希望する色
茶系
■ 選んだ理由

デザイン性、サイト特徴の訴求性、バランスの3点で各評価の一番高いもの、
総合で良かった2点を当選させて頂きました。
社内でアンケートを取りまして、結果5件を採用とさせていただきました。

■ 提案者全員のお礼・コメント

たくさんのご提案をいただきまして、誠にありがとうございました。
みなさま素晴らしいご提案ばかりで、とても迷いました。
採用できなかった方へは大変心苦しいですが、こちらで募集をしてよかったです。
また機会がございましたら、ぜひよろしくお願いいたします。

```html
<!DOCTYPE html>
<html lang="ja">
<head>
<meta charset="utf-8">
<title>高級賃貸の碧泉荘館 バナー</title>
<link rel="stylesheet" href="https://fonts.googleapis.com/css2?family=Noto+Serif+JP:wght@700;900&family=Noto+Sans+JP:wght@300;400;700&display=swap">
<style>
  :root {
    --navy: #1b2a5c;
    --navy-deep: #16234d;
    --yellow: #f3e34c;
    --white: #ffffff;
    --photo-light: #d9d6d0;
    --photo-mid: #a9a49c;
    --photo-dark: #6e6a64;
  }
  html, body {
    margin: 0;
    padding: 0;
    width: 1200px;
    height: 4500px;
    overflow: hidden;
    background: var(--white);
  }
  .banner {
    position: relative;
    width: 1200px;
    height: 4500px;
    overflow: hidden;
    font-family: "Noto Serif JP", serif;
  }
  .room-photo {
    position: absolute;
    left: 0; top: 0;
    width: 1200px;
    height: 3700px;
    background:
      linear-gradient(180deg, rgba(40,40,45,0.35) 0%, rgba(40,40,45,0.15) 40%, rgba(40,40,45,0.3) 100%),
      linear-gradient(100deg, var(--photo-dark) 0%, var(--photo-mid) 30%, var(--photo-light) 60%, var(--photo-mid) 85%, var(--photo-dark) 100%);
  }
  .tagline-band {
    position: absolute;
    left: 812px; top: 0;
    width: 240px;
    height: 2220px;
    background: var(--navy);
    display: flex;
    justify-content: center;
    padding-top: 230px;
    box-sizing: border-box;
  }
  .tagline {
    writing-mode: vertical-rl;
    margin: 0;
    font-size: 96px;
    font-weight: 900;
    line-height: 1;
    letter-spacing: 14px;
    color: var(--white);
  }
  .tagline .accent { color: var(--yellow); }
  .fee-copy {
    position: absolute;
    left: 496px; top: 280px;
    writing-mode: vertical-rl;
    margin: 0;
    font-size: 124px;
    font-weight: 900;
    line-height: 1;
    letter-spacing: 10px;
    color: var(--white);
    text-shadow: 0 0 24px rgba(0,0,0,0.55);
  }
  .fee-copy .max {
    display: inline-block;
    border: 7px solid var(--white);
    padding: 16px 8px;
    margin: 18px 0;
  }
  .site-headline {
    position: absolute;
    left: 166px; top: 380px;
    writing-mode: vertical-rl;
    margin: 0;
    font-size: 228px;
    font-weight: 900;
    line-height: 1;
    letter-spacing: 22px;
    color: var(--white);
    text-shadow: 0 0 32px rgba(0,0,0,0.55);
  }
  .listing-note {
    position: absolute;
    left: 60px; top: 3480px;
    width: 1080px;
    height: 150px;
    box-sizing: border-box;
    background: var(--white);
    border: 8px solid var(--navy);
    display: flex;
    align-items: center;
    justify-content: center;
    margin: 0;
    font-family: "Noto Sans JP", sans-serif;
    font-weight: 700;
    font-size: 80px;
    letter-spacing: 4px;
    color: var(--navy);
  }
  .brand-block {
    position: absolute;
    left: 0; top: 3690px;
    width: 1200px;
    height: 810px;
    background: var(--navy-deep);
    color: var(--white);
    font-family: "Noto Sans JP", sans-serif;
  }
  .brand-lead {
    position: absolute;
    left: 120px; top: 100px;
    margin: 0;
    font-size: 80px;
    font-weight: 400;
    line-height: 1;
    letter-spacing: 4px;
  }
  .brand-name {
    position: absolute;
    left: 110px; top: 270px;
    margin: 0;
    font-size: 210px;
    font-weight: 300;
    line-height: 1;
    letter-spacing: 40px;
  }
  .brand-sub {
    position: absolute;
    left: 0; top: 610px;
    width: 1200px;
    margin: 0;
    text-align: center;
    font-size: 38px;
    font-weight: 400;
    letter-spacing: 14px;
  }
</style>
</head>
<body>
  <main class="banner">
    <div class="room-photo" role="img" aria-label="明るい高級マンションのリビング。ソファとガラスのテーブルが並ぶ室内"></div>

    <div class="tagline-band">
      <p class="tagline"><span class="accent">都心</span>の<span class="accent">高級賃貸マンション</span>を探すなら</p>
    </div>

    <p class="fee-copy">仲介料<span class="max">最大</span>無料</p>
    <h1 class="site-headline">都内高級賃貸検索サイト</h1>

    <p class="listing-note">優良物件を多数掲載</p>

    <footer class="brand-block">
      <p class="brand-lead">高級賃貸の</p>
      <p class="brand-name">碧泉荘館</p>
      <p class="brand-sub">LUXURY RESIDENCE SELECTION</p>
    </footer>
  </main>
</body>
</html>
```